Messianic Prophetic Timeline

I would like to create a timeline that will fit on a horizontal 11 x 8 1/2 (8 1/2 x11) sheet of paper.
I have two images that will need to be merged.
There should be 7 time points. 1) 457BCE-26 AD, 2) 26 AD-30AD, 3) 30 AD-66 AD, 4) 66AD- 70AD 5) 70 AD, 6) 70AD-20??, and 7) Future
The #6 and #7 from each graphic should be merged. The 30AD-70AD can be dropped. Time point #7 Future has two different texts both need to be preserved, I would like time point #7 to be larger than the other time points.
There are scripture verses that are associated with each block that should be preserved and be more prominent.
These images are from a powerpoint slide, but I want something that can be printed out.
I run a website www.brightfieldlamp.org. I have some brand colors that if can be incorporated or at least have some color cohesion would be great, but that is not as important as readability.
Background images are nice - The idea is one of conflict between light and darkness, two opposing forces, Christ and anti-Christ. Maybe a king on a white horse battling a large serpent dragon
If you can incorporate this quote near timeblock #1-2 "From the decree to restore Jerusalem until Messiah 483 year"
Second quote anywhere "He will make a covenant with many for 7 years"

```html
<!DOCTYPE html>
<html lang="en">
<head>
<meta charset="utf-8">
<title>Messianic Prophetic Timeline</title>
<link href="https://fonts.googleapis.com/css2?family=Poppins:ital,wght@0,300;0,400;0,600;0,700;1,300;1,400&display=swap" rel="stylesheet">
<style>
  :root{
    --bg:#000;
    --road:#2f2f2f;
    --text:#fff;
    --muted:#d9d9d9;
    --c1:#7fd9d6;
    --c2:#ff9f2e;
    --c3:#00c6f2;
    --c4:#d43a0a;
    --c5:#15b1b1;
    --c6:#fbb614;
    --c7:#00cdd4;
    --ink:#111;
    --web:#1fc8d0;
  }
  html,body{margin:0;padding:0;overflow:hidden;background:var(--bg);}
  .sheet{
    position:relative;width:1200px;height:929px;overflow:hidden;
    background:var(--bg);font-family:"Poppins",sans-serif;color:var(--text);
  }
  .road{position:absolute;inset:0;}
  .portrait{
    position:absolute;left:63px;top:60px;width:96px;height:94px;
    background:radial-gradient(ellipse at 50% 45%,#e8e8e8 0%,#8a8a8a 55%,#000 75%);
    border-radius:50% 50% 45% 45%;
  }
  .title{
    position:absolute;left:184px;top:78px;margin:0;
    font-weight:700;font-size:28px;line-height:32px;letter-spacing:1.5px;
  }
  .badge{
    position:absolute;height:41px;border-radius:6px;
    display:flex;align-items:center;justify-content:center;
    font-weight:700;font-size:19px;color:#fff;letter-spacing:.3px;
  }
  .badge.dark{color:var(--ink);}
  .entry{position:absolute;}
  .entry h3{
    position:relative;margin:0;font-weight:700;font-size:19.5px;line-height:24px;
  }
  .entry h3::before{
    content:"";position:absolute;left:-16px;top:6px;
    border-left:9px solid var(--accent);border-top:6.5px solid transparent;border-bottom:6.5px solid transparent;
  }
  .entry p{margin:0;font-weight:300;font-size:15.5px;line-height:18.7px;color:var(--text);}
  .entry .rule{height:2.5px;width:127px;background:var(--accent);margin:10px 0 8px;}
  .entry .refs{font-style:italic;font-weight:300;font-size:14.5px;line-height:17px;color:var(--muted);}
  .decree-quote{
    position:absolute;left:180px;top:618px;width:170px;margin:0;
    font-size:13.5px;line-height:17px;color:var(--muted);font-weight:300;
    transform:rotate(-16deg);transform-origin:center;
  }
  .covenant-quote{
    position:absolute;right:68px;top:765px;margin:0;text-align:right;
    font-weight:300;font-size:21px;line-height:26px;
  }
  .quote-bar{position:absolute;left:1067px;top:750px;width:61px;height:13px;background:#e6e6e6;}
  .site{
    position:absolute;left:677px;top:830px;margin:0;
    font-size:17px;letter-spacing:10.6px;color:var(--web);font-weight:400;
  }
</style>
</head>
<body>
<div class="sheet">
  <svg class="road" viewBox="0 0 1200 929" width="1200" height="929" aria-hidden="true">
    <defs>
      <linearGradient id="beam" x1="1" y1="0" x2="0.3" y2="0.6">
        <stop offset="0" stop-color="#fff" stop-opacity=".35"/>
        <stop offset=".5" stop-color="#fff" stop-opacity=".08"/>
        <stop offset="1" stop-color="#fff" stop-opacity="0"/>
      </linearGradient>
    </defs>
    <polygon points="1200,0 1140,0 300,700 800,900 1200,160" fill="url(#beam)"/>
    <polygon points="0,673 588,511 709,522 0,810" fill="var(--road)"/>
    <path d="M600 510 C 740 490, 760 472, 690 470 L 235 468 C 170 466, 175 413, 245 411 L 925 380 C 1000 375, 1000 335, 925 334 L 420 326 C 350 324, 355 290, 450 287 L 1200 262"
          fill="none" stroke="var(--road)" stroke-width="44" stroke-linecap="butt"/>

    <g class="pin">
      <line x1="122.5" y1="654" x2="122.5" y2="717" stroke="var(--c1)" stroke-width="4"/>
      <circle cx="122.5" cy="654" r="33" fill="var(--c1)"/>
      <circle cx="122.5" cy="654" r="17.5" fill="#fff"/>
      <text x="122.5" y="660" text-anchor="middle" font-family="Poppins,sans-serif" font-weight="700" font-size="16" fill="#111">01</text>
    </g>
    <g class="pin">
      <line x1="391" y1="568" x2="391" y2="618" stroke="var(--c2)" stroke-width="4"/>
      <circle cx="391" cy="568" r="26.5" fill="var(--c2)"/>
      <circle cx="391" cy="568" r="15" fill="#fff"/>
      <text x="391" y="574" text-anchor="middle" font-family="Poppins,sans-serif" font-weight="700" font-size="15" fill="#111">02</text>
    </g>
    <g class="pin">
      <line x1="609" y1="495" x2="609" y2="546" stroke="var(--c3)" stroke-width="4"/>
      <circle cx="609" cy="495" r="27.5" fill="var(--c3)"/>
      <circle cx="609" cy="495" r="15.5" fill="#fff"/>
      <text x="609" y="501" text-anchor="middle" font-family="Poppins,sans-serif" font-weight="700" font-size="15" fill="#111">03</text>
    </g>
    <g class="pin">
      <line x1="225" y1="375" x2="225" y2="434" stroke="var(--c4)" stroke-width="4"/>
      <circle cx="225" cy="375" r="31" fill="var(--c4)"/>
      <circle cx="225" cy="375" r="17" fill="#fff"/>
      <text x="225" y="381" text-anchor="middle" font-family="Poppins,sans-serif" font-weight="700" font-size="15" fill="#111">04</text>
    </g>
    <g class="pin">
      <line x1="785" y1="357" x2="785" y2="404" stroke="var(--c5)" stroke-width="4"/>
      <circle cx="785" cy="357" r="25" fill="var(--c5)"/>
      <circle cx="785" cy="357" r="14.5" fill="#fff"/>
      <text x="785" y="363" text-anchor="middle" font-family="Poppins,sans-serif" font-weight="700" font-size="15" fill="#111">05</text>
    </g>
    <g class="pin">
      <line x1="509" y1="236" x2="509" y2="288" stroke="var(--c6)" stroke-width="4"/>
      <circle cx="509" cy="236" r="28.5" fill="var(--c6)"/>
      <circle cx="509" cy="236" r="16" fill="#fff"/>
      <text x="509" y="242" text-anchor="middle" font-family="Poppins,sans-serif" font-weight="700" font-size="15" fill="#111">06</text>
    </g>
    <g class="pin">
      <line x1="855" y1="165" x2="855" y2="264" stroke="var(--c7)" stroke-width="5"/>
      <circle cx="855" cy="165" r="52" fill="var(--c7)"/>
      <circle cx="855" cy="165" r="28.5" fill="#fff"/>
      <text x="855" y="177" text-anchor="middle" font-family="Poppins,sans-serif" font-weight="700" font-size="30" fill="#111">07</text>
    </g>
  </svg>

  <div class="portrait" role="img" aria-label="Portrait illustration of Christ in white on black"></div>
  <h1 class="title">MESSIANIC<br>PROPHETIC TIMELINE</h1>

  <p class="decree-quote">"From the decree to restore Jerusalem until Messiah 483 year”</p>

  <div class="badge dark" style="left:172px;top:699px;width:160px;background:var(--c1)">457BC - 26AD</div>
  <div class="entry" style="left:175px;top:746px;--accent:var(--c1)">
    <h3>Messiah Cut Off</h3>
    <p>483 years from<br>decree</p>
    <div class="rule"></div>
    <div class="refs">Daniel 9:26, Ezra 7,9:9</div>
  </div>

  <div class="badge" style="left:419px;top:603px;width:151px;background:var(--c2)">26AD - 30AD</div>
  <div class="entry" style="left:424px;top:652px;--accent:var(--c2)">
    <h3>Covenant Made</h3>
    <p>Jesus makes<br>covenant with<br>many, stops</p>
    <div class="rule"></div>
    <div class="refs">Daniel 9:27</div>
  </div>

  <div class="badge" style="left:643px;top:524px;width:160px;background:var(--c3)">30AD - 66AD</div>
  <div class="entry" style="left:646px;top:575px;--accent:var(--c3)">
    <h3>Apostles Percecution</h3>
    <p>in Synagogue by<br>family, friends and<br>by Kings</p>
    <div class="rule"></div>
    <div class="refs">Luke 21:12-19</div>
  </div>

  <div class="badge" style="left:274px;top:358px;width:155px;background:var(--c4)">66AD - 70AD</div>
  <div class="entry" style="left:285px;top:406px;--accent:var(--c4)">
    <h3>Vengeance Days of Jerusalem</h3>
    <p>Surrounded<br>Flee</p>
    <div class="rule"></div>
    <div class="refs">Luke 21:20-23</div>
  </div>

  <div class="badge" style="left:818px;top:404px;width:89px;background:var(--c5)">70AD</div>
  <div class="entry" style="left:819px;top:448px;--accent:var(--c5)">
    <h3>Jerusalem Desolation</h3>
    <p>Dispersed in Nations</p>
    <div class="rule"></div>
    <div class="refs">Luke 21:24, Is. 61:2, Hos. 9:27</div>
  </div>

  <div class="badge" style="left:575px;top:215px;width:131px;background:var(--c6)">70AD - 20?</div>
  <div class="entry" style="left:578px;top:260px;--accent:var(--c6)">
    <h3>Gentiles Time</h3>
    <p>Trample Jerusalem</p>
    <div class="rule"></div>
    <div class="refs">Luke 21: 8-11, 24<br>Matt. 24: 4-14</div>
  </div>

  <div class="badge dark" style="left:945px;top:141px;width:108px;background:var(--c7)">FUTURE</div>
  <div class="entry" style="left:946px;top:188px;--accent:var(--c7)">
    <h3>Covenant Made</h3>
    <p>Stops Sacrifice Causes<br>Abomination of Desolation</p>
    <h3 style="margin-top:10px">Abomination of<br>Desolation</h3>
    <p>Signs in Sun, moon, stars.<br>Jesus returns</p>
    <div class="rule"></div>
    <div class="refs">Luke 21:25, Matt 24:15,<br>Dan 9:27, 11:31, 12:11</div>
  </div>

  <div class="quote-bar"></div>
  <p class="covenant-quote">"He will make a covenant<br>with many for 7 years”</p>
  <p class="site">www.brightfieldlamp.org</p>
</div>
</body>
</html>
```